Maplecrest Insurance Services - Application Designs

My company name is Maplecrest Insurance Services. We are a full service insurance brokerage.

I need an ACH Form (which is attached) to be created with my logo (which is also attached). Please make the ACH Form fillable for info to be entered manually.

In addition I need the Example Quote created with the same color scheme as the Maplecrest Logo. Please create the Example quote as a word document so I can edit the quote and save as a PDF. You can also send me different quote ideas as long as they have the same information on the quote I have attached.

For the Example Supplemental you can leave everything as is and just change the Tillmoor Logo to the attached Maplecrest Insurance Services Logo.

- Change all color-ways to the Maplecrest Insurance Services color-way logo
- Change all the Tillmoor logos to the Maplecrest logo
- Phone number to the company is (555) 317-2096
- Change anything that says Tillmoor to Maplecrest
- Company address is: 7810 Pellway Ave, Unit D Fernhaven CA 93480
- Company Email address is Dana@Maplecrestinsuranceservices.example

Target Market(s)

Clients or Potential Clients

Industry/Entity Type

Insurance

Font styles to use
Serif

Colors
0054AA
0677BA
7BADD7
CADEEF
E8F1F8
00AB8E
00BBA5
67D7C9
C6EFE9
E9F9F6

Requirements
Must have
• Maplecrest Insurance Services Logo

```html
<!DOCTYPE html>
<html lang="en">
<head>
<meta charset="utf-8">
<title>Maplecrest Insurance Services – Supplemental Application</title>
<link href="https://fonts.googleapis.com/css2?family=Carlito:wght@400;700&display=swap" rel="stylesheet">
<style>
  :root{
    --brand-navy:#0054AA;
    --brand-blue:#0677BA;
    --ink:#231f20;
    --rule:#231f20;
    --header-fill:#a6a6a6;
    --muted:#6b6b6b;
    --paper:#ffffff;
  }
  *{box-sizing:border-box;margin:0;padding:0}
  html,body{width:927px;height:1200px;overflow:hidden;background:var(--paper)}
  body{font-family:"Carlito",sans-serif;color:var(--ink)}
  .page{position:relative;width:927px;height:1200px;overflow:hidden}

  .brand-name{position:absolute;left:55px;top:58px;width:360px;font-size:40px;line-height:44px;font-weight:700;color:var(--brand-navy);letter-spacing:.5px}
  .agency-contact{position:absolute;right:70px;top:46px;text-align:right;font-size:15px;line-height:18px;font-style:normal}
  .agency-contact .agency-title{font-weight:700}

  .field-label{position:absolute;font-size:15px;font-weight:700}
  .field-line{position:absolute;height:0;border-bottom:1px solid var(--rule)}
  .instruction{position:absolute;left:55px;top:223px;font-size:13.5px;font-weight:700}

  .payroll{position:absolute;left:55px;top:252px;width:810px;border-collapse:collapse;font-size:11.5px}
  .payroll td,.payroll th{border:1px solid var(--rule);text-align:left;padding:0 6px;font-weight:400}
  .payroll th{height:25px;font-size:15px;font-weight:700}
  .payroll th.corner{background:var(--header-fill);width:106px}
  .payroll td{height:23.4px}
  .payroll th.payroll-col{width:352px}

  .section-title{position:absolute;left:55px;font-size:15px;font-weight:700;letter-spacing:.2px}

  .form-table{position:absolute;left:55px;width:811px;border:1px solid var(--rule)}
  .form-row{position:relative;height:18px;border-top:1px solid var(--rule);font-size:11.5px;line-height:16px}
  .form-row:first-child{border-top:0}
  .form-row.tall{height:54px}
  .form-row > *{position:absolute;top:1px;white-space:nowrap}
  .label{left:1px}
  .at{left:var(--x)}
  .split{position:absolute;left:403px;top:0;bottom:0;border-left:1px solid var(--rule)}
  .blank{display:inline-block;border-bottom:1px solid var(--rule);height:11px;vertical-align:top}

  .choices{display:flex}
  .opt{display:flex;align-items:center;width:54px}
  .box{width:17px;height:12px;border:1.3px solid var(--ink);margin-right:6px;flex:none;margin-top:2px}

  .page-number{position:absolute;left:0;width:927px;top:1136px;text-align:center;font-size:14px;font-weight:700}
  .revision{position:absolute;right:62px;top:1135px;font-size:7.5px;color:var(--muted)}
</style>
</head>
<body>
<main class="page">

  <div class="brand-name">Maplecrest<br>Insurance Services</div>

  <address class="agency-contact">
    <div class="agency-title">Maplecrest Insurance Services</div>
    <div>7810 Pellway Ave,</div>
    <div>Unit D Fernhaven</div>
    <div>CA 93480</div>
    <div>Tel: (555) 317-2096</div>
    <div>E-mail: Dana@Maplecrestinsuranceservices.example</div>
  </address>

  <span class="field-label" style="left:55px;top:174px">Insured Name:</span>
  <span class="field-line" style="left:172px;width:360px;top:191px"></span>
  <span class="field-label" style="left:55px;top:199px">Web Site:</span>
  <span class="field-line" style="left:162px;width:427px;top:215px"></span>
  <span class="field-label" style="left:607px;top:199px">FEIN:</span>
  <span class="field-line" style="left:658px;width:202px;top:215px"></span>

  <p class="instruction">Applicant must complete pages 1, 2 and the sections pertinent.</p>

  <table class="payroll">
    <tr><th class="corner"></th><th class="payroll-col">Payroll Information</th><th>Premium Information</th></tr>
    <tr><td>Current Year</td><td></td><td></td></tr>
    <tr><td>Prior Year</td><td></td><td></td></tr>
    <tr><td>Prior Year</td><td></td><td></td></tr>
    <tr><td>Prior Year</td><td></td><td></td></tr>
    <tr><td>Prior Year</td><td></td><td></td></tr>
  </table>

  <h2 class="section-title" style="top:406px">OPERATIONAL INFORMATION</h2>
  <section class="form-table" style="top:426px">
    <div class="form-row tall"><span class="label">Description of operations (if not provided on Form WQ-130):</span></div>
    <div class="form-row">
      <span class="label">Hours of operation:</span>
      <span class="at" style="--x:228px"># of shifts: <span class="blank" style="width:100px;margin-left:10px"></span></span>
      <span class="at" style="--x:539px">Any 24 hr exposure:</span>
      <span class="at choices" style="--x:697px"><span class="opt"><i class="box"></i>Yes</span><span class="opt"><i class="box"></i>No</span></span>
    </div>
    <div class="form-row">
      <span class="label"># of years in business:</span>
      <span class="at" style="--x:228px">Average employee tenure with company: <span class="blank" style="width:100px;margin-left:10px"></span></span>
    </div>
    <div class="form-row">
      <span class="label">Have you ever filed for bankruptcy within the past 7 years:</span>
      <span class="at choices" style="--x:318px"><span class="opt"><i class="box"></i>Yes</span><span class="opt"><i class="box"></i>No</span></span>
    </div>
  </section>

  <h2 class="section-title" style="top:566px">SAFETY INFORMATION</h2>
  <section class="form-table" style="top:589px">
    <div class="form-row"><span class="label">Active IIPP:</span>
      <span class="at choices" style="--x:231px"><span class="opt"><i class="box"></i>Yes</span><span class="opt"><i class="box"></i>No</span></span>
      <i class="split"></i><span class="at" style="--x:405px">Active ownership in operations:</span>
      <span class="at choices" style="--x:698px"><span class="opt"><i class="box"></i>Yes</span><span class="opt"><i class="box"></i>No</span></span></div>
    <div class="form-row"><span class="label">Specific job training:</span>
      <span class="at choices" style="--x:231px"><span class="opt"><i class="box"></i>Yes</span><span class="opt"><i class="box"></i>No</span><span class="opt"><i class="box"></i>N/A</span></span>
      <i class="split"></i><span class="at" style="--x:405px">Personal protective equipment:</span>
      <span class="at choices" style="--x:698px"><span class="opt"><i class="box"></i>Yes</span><span class="opt"><i class="box"></i>No</span></span></div>
    <div class="form-row"><span class="label">Respiratory program:</span>
      <span class="at choices" style="--x:231px"><span class="opt"><i class="box"></i>Yes</span><span class="opt"><i class="box"></i>No</span><span class="opt"><i class="box"></i>N/A</span></span>
      <i class="split"></i><span class="at" style="--x:405px">If yes, type of PPE:</span></div>
    <div class="form-row"><span class="label">Safety incentives:</span>
      <span class="at choices" style="--x:231px"><span class="opt"><i class="box"></i>Yes</span><span class="opt"><i class="box"></i>No</span><span class="opt"><i class="box"></i>N/A</span></span>
      <i class="split"></i><span class="at" style="--x:405px">Formal return to work program:</span>
      <span class="at choices" style="--x:698px"><span class="opt"><i class="box"></i>Yes</span><span class="opt"><i class="box"></i>No</span></span></div>
    <div class="form-row"><span class="label">Monthly safety meetings:</span>
      <span class="at choices" style="--x:231px"><span class="opt"><i class="box"></i>Yes</span><span class="opt"><i class="box"></i>No</span><span class="opt"><i class="box"></i>N/A</span></span></div>
    <div class="form-row"><span class="label">Do you have a written safety manual:</span>
      <span class="at choices" style="--x:231px"><span class="opt"><i class="box"></i>Yes</span><span class="opt"><i class="box"></i>No</span></span></div>
    <div class="form-row"><span class="label">Is it provided to all employees in:</span>
      <span class="at choices" style="--x:231px"><span class="opt" style="width:74px"><i class="box"></i>English</span><span class="opt" style="width:77px"><i class="box"></i>Spanish</span><span class="opt" style="width:90px"><i class="box"></i>Other/Multi</span></span></div>
    <div class="form-row"><span class="label">Safety Director:</span>
      <span class="at choices" style="--x:231px"><span class="opt"><i class="box"></i>Yes</span><span class="opt"><i class="box"></i>No</span><span class="opt"><i class="box"></i>N/A</span></span></div>
    <div class="form-row"><span class="label">Risk manager employed:</span>
      <span class="at choices" style="--x:231px"><span class="opt"><i class="box"></i>Yes</span><span class="opt"><i class="box"></i>No</span><span class="opt"><i class="box"></i>N/A</span></span></div>
    <div class="form-row"><span class="label">Do supervisors receive specific safety training:</span>
      <span class="at choices" style="--x:336px"><span class="opt"><i class="box"></i>Yes</span><span class="opt"><i class="box"></i>No</span><span class="opt"><i class="box"></i>N/A</span></span></div>
    <div class="form-row"><span class="label">Supervisors held accountable for injuries:</span>
      <span class="at choices" style="--x:336px"><span class="opt"><i class="box"></i>Yes</span><span class="opt"><i class="box"></i>No</span><span class="opt"><i class="box"></i>N/A</span></span></div>
    <div class="form-row"><span class="label">Condition of workplace premises:</span>
      <span class="at choices" style="--x:336px"><span class="opt" style="width:63px"><i class="box"></i>Good</span><span class="opt" style="width:76px"><i class="box"></i>Average</span><span class="opt"><i class="box"></i>Poor</span></span></div>
    <div class="form-row"><span class="label">Accident investigation program in place:</span>
      <span class="at choices" style="--x:336px"><span class="opt"><i class="box"></i>Yes</span><span class="opt"><i class="box"></i>No</span><span class="opt"><i class="box"></i>N/A</span></span></div>
    <div class="form-row"><span class="label">Written Lockout/Tagout/Blockout Procedure in place:</span>
      <span class="at choices" style="--x:336px"><span class="opt"><i class="box"></i>Yes</span><span class="opt"><i class="box"></i>No</span><span class="opt"><i class="box"></i>N/A</span></span></div>
    <div class="form-row"><span class="label">Material Safety Data Sheet available:</span>
      <span class="at choices" style="--x:336px"><span class="opt"><i class="box"></i>Yes</span><span class="opt"><i class="box"></i>No</span><span class="opt"><i class="box"></i>N/A</span></span></div>
    <div class="form-row"><span class="label">Hazardous Materials Communication program in place:</span>
      <span class="at choices" style="--x:336px"><span class="opt"><i class="box"></i>Yes</span><span class="opt"><i class="box"></i>No</span><span class="opt"><i class="box"></i>N/A</span></span></div>
    <div class="form-row"><span class="label">Have Cal/OHSA cited risk’s business in the last year:</span>
      <span class="at choices" style="--x:336px"><span class="opt"><i class="box"></i>Yes</span><span class="opt"><i class="box"></i>No</span><span class="opt"><i class="box"></i>N/A</span></span></div>
    <div class="form-row"><span class="label">Is insured willing to implement loss control recommendations made by the insurer:</span>
      <span class="at choices" style="--x:443px"><span class="opt"><i class="box"></i>Yes</span><span class="opt"><i class="box"></i>No</span></span></div>
    <div class="form-row"><span class="label">Are employee required breaks in the work hours strictly adhered to for all employees:</span>
      <span class="at choices" style="--x:443px"><span class="opt"><i class="box"></i>Yes</span><span class="opt"><i class="box"></i>No</span></span></div>
    <div class="form-row"><span class="label">Is training provided to new hires and existing employees on proper use and maintenance of equipment:</span>
      <span class="at choices" style="--x:636px"><span class="opt"><i class="box"></i>Yes</span><span class="opt"><i class="box"></i>No</span></span></div>
    <div class="form-row"><span class="label">Are all employees that operate forklifts properly trained, if applicable:</span>
      <span class="at choices" style="--x:443px"><span class="opt"><i class="box"></i>Yes</span><span class="opt"><i class="box"></i>No</span><span class="opt"><i class="box"></i>N/A</span></span></div>
    <div class="form-row"><span class="label">Has your company implemented any ergonomic safety procedures:</span>
      <span class="at choices" style="--x:336px"><span class="opt"><i class="box"></i>Yes</span><span class="opt"><i class="box"></i>No</span></span>
      <span class="at" style="--x:445px">Describe:</span></div>
    <div class="form-row"><span class="label">Describe equipment used:</span>
      <span class="at choices" style="--x:155px"><span class="opt" style="width:110px"><i class="box"></i>State of the art</span><span class="opt" style="width:140px"><i class="box"></i>Standard for industry</span><span class="opt" style="width:130px"><i class="box"></i>Modified to standard</span></span></div>
  </section>

  <div class="page-number">1</div>
  <div class="revision">REV 12.1.16</div>
</main>
</body>
</html>
```